DOG DAYCARE BILLBOARD

Design a bold exciting billboard that can be read easily from a distance! Our goal is brand awareness and showcasing the services we offer (Boarding, Grooming, Daycare, and Training.
we would like to see examples with the phrase "your best friend's best day". Our name Bright Meadow Canine Activity Center (or just Bright Meadow might work better and could be bigger) and the services we provide.
(there are two examples of what we like included in the pictures)
you can find more information o our website at pawplayhouse@mailbox-example.com.

```html
<!DOCTYPE html>
<html lang="en">
<head>
<meta charset="utf-8">
<title>Bright Meadow Billboard</title>
<link href="https://fonts.googleapis.com/css2?family=Bebas+Neue&family=Montserrat:wght@600;800&display=swap" rel="stylesheet">
<style>
  :root {
    --lime: #b2d235;
    --ink: #000000;
    --paper: #ffffff;
    --backdrop: #eef1f4;
    --photo-light: #f2f2f0;
    --photo-dark: #c9c9c4;
  }
  html, body {
    margin: 0;
    padding: 0;
    width: 1200px;
    height: 903px;
    overflow: hidden;
    background: var(--backdrop);
  }
  .billboard {
    position: absolute;
    left: 20px;
    top: 183px;
    width: 1160px;
    height: 536px;
    background: var(--lime);
    overflow: hidden;
  }
  .headline {
    position: absolute;
    top: 172px;
    margin: 0;
    font-family: "Bebas Neue", "Oswald", sans-serif;
    font-weight: 400;
    font-size: 96px;
    line-height: 1;
    color: var(--ink);
    white-space: nowrap;
    transform: scaleY(1.08);
    transform-origin: top left;
  }
  .headline--lead { left: 54px; letter-spacing: 0.5px; }
  .headline--tail { left: 832px; letter-spacing: 0.5px; }
  .puppy-photo {
    position: absolute;
    left: 659px;
    top: 17px;
    width: 190px;
    height: 355px;
    border-radius: 80px 80px 16px 16px;
    background: linear-gradient(180deg, var(--photo-light) 0%, var(--photo-dark) 100%);
  }
  .service-band {
    position: absolute;
    left: 0;
    bottom: 0;
    width: 100%;
    height: 118px;
    background: var(--ink);
    display: flex;
    align-items: center;
    justify-content: space-between;
    padding: 36px 52px 0 52px;
    box-sizing: border-box;
  }
  .service {
    font-family: "Montserrat", sans-serif;
    font-weight: 600;
    font-size: 46px;
    color: var(--paper);
    white-space: nowrap;
  }
  .divider {
    width: 4px;
    height: 44px;
    background: var(--lime);
  }
  .brand-plate {
    position: absolute;
    left: 291px;
    top: 383px;
    width: 578px;
    height: 58px;
    background: var(--paper);
    display: flex;
    align-items: center;
    justify-content: center;
    z-index: 2;
  }
  .brand-name {
    font-family: "Montserrat", sans-serif;
    font-weight: 800;
    font-size: 40px;
    letter-spacing: 0.12em;
    color: var(--ink);
    white-space: nowrap;
  }
</style>
</head>
<body>
  <main class="billboard">
    <h1 class="headline headline--lead">YOUR BEST FRIEND'S</h1>
    <div class="puppy-photo" role="img" aria-label="Photo of a seated Dalmatian puppy"></div>
    <span class="headline headline--tail">BEST DAY</span>

    <div class="brand-plate">
      <span class="brand-name">BRIGHT MEADOW</span>
    </div>

    <div class="service-band">
      <span class="service">Boarding</span>
      <span class="divider"></span>
      <span class="service">Grooming</span>
      <span class="divider"></span>
      <span class="service">Daycare</span>
      <span class="divider"></span>
      <span class="service">Training</span>
    </div>
  </main>
</body>
</html>
```